Showroom Quote Web Application - Prism Layout wanted

This web app is an internal application that will be used by one of our customers to build quotes and produce orders of retail items with their customers

the overall design should use the colour pallet provided and have a clean and simple interface

we'd like to go with a prism layout type of look

attached mockups are just a rough stab at some layouts to give you an example, please feel free to reach out with any questions.

Please don't get hung up on the specific pages, they were intended to provide context, we are looking for a high level design using the provided colour schemes and fonts, additional work may follow for the selected designer when it comes to specific pages or work flows.

Sorry for the short timeline, we have a tight deadline on this one.

Target Market(s)

internal application for customer

Industry/Entity Type

Retail

Other font styles liked:
• see attached doc for fonts

Requirements
Must have
• simple and clean interface
• intuitive design
Nice to have
• see attached documents for logo colour schemes and fonts
• these must be incorporated into the design

```html
<!DOCTYPE html>
<html lang="en">
<head>
<meta charset="utf-8">
<title>Tapline – Log In</title>
<link rel="stylesheet" href="https://fonts.googleapis.com/css2?family=Source+Sans+3:wght@300;400;600;700&display=swap">
<style>
  :root {
    --bg: #0a377a;
    --bg-deep: #082f6a;
    --badge: #0a3270;
    --line: rgba(255,255,255,0.75);
    --text: #ffffff;
    --muted: #c9d3e4;
    --button: #ffffff;
    --button-text: #0b3577;
  }
  * { box-sizing: border-box; margin: 0; padding: 0; }
  html, body { width: 675px; height: 1200px; overflow: hidden; }
  body {
    position: relative;
    background: var(--bg);
    font-family: "Source Sans 3", "Myriad Pro", sans-serif;
    color: var(--text);
  }
  .backdrop { position: absolute; inset: 0; }
  .status-bar {
    position: absolute; top: 0; left: 0; right: 0; height: 62px;
    display: flex; align-items: center; justify-content: space-between;
    padding: 0 14px; font-size: 20px; font-weight: 400;
  }
  .status-left, .status-right { display: flex; align-items: center; gap: 6px; }
  .status-time { position: absolute; left: 50%; transform: translateX(-50%); font-weight: 600; }
  .brand-badge {
    position: absolute; left: 187px; top: 207px; width: 300px; height: 300px;
    border-radius: 50%; background: var(--badge);
    display: flex; align-items: center; justify-content: center;
  }
  .brand-name { font-size: 32px; font-weight: 700; letter-spacing: 1px; }
  .login-form { position: absolute; left: 90px; top: 594px; width: 490px; }
  .field {
    height: 86px; border: 1px solid var(--line); border-radius: 13px;
    display: flex; align-items: center; padding-left: 30px; gap: 18px;
    font-size: 27px; font-weight: 300; color: var(--muted);
    margin-bottom: 21px;
  }
  .field svg { flex: none; }
  .login-button {
    margin-top: 26px; width: 486px; height: 100px; border-radius: 5px;
    background: var(--button); color: var(--button-text);
    display: flex; align-items: center; justify-content: center;
    font-size: 32px; font-weight: 700; letter-spacing: 0.5px;
  }
  .register-line {
    margin-top: 30px; width: 486px; text-align: center;
    font-size: 21px; font-weight: 400;
  }
  .register-line strong { font-weight: 700; }
</style>
</head>
<body>
  <svg class="backdrop" width="675" height="1200" viewBox="0 0 675 1200" aria-hidden="true">
    <polygon points="0,0 675,0 675,1200 0,1200" fill="var(--bg)"/>
    <polygon points="0,585 160,650 190,690 0,790" fill="var(--bg-deep)" opacity="0.5"/>
    <polygon points="0,840 675,480 675,580 0,950" fill="var(--bg-deep)" opacity="0.55"/>
    <polygon points="0,975 675,1165 675,1200 0,1200" fill="var(--bg-deep)" opacity="0.45"/>
    <polygon points="0,0 30,0 30,1200 0,1200" fill="var(--bg-deep)" opacity="0.35"/>
    <polygon points="645,0 675,0 675,1200 645,1200" fill="var(--bg-deep)" opacity="0.35"/>
  </svg>

  <header class="status-bar">
    <div class="status-left">
      <svg width="74" height="12" viewBox="0 0 74 12" aria-hidden="true">
        <circle cx="6" cy="6" r="5" fill="#fff"/><circle cx="20" cy="6" r="5" fill="#fff"/>
        <circle cx="34" cy="6" r="5" fill="#fff"/>
        <circle cx="48" cy="6" r="4.5" fill="none" stroke="#fff"/><circle cx="62" cy="6" r="4.5" fill="none" stroke="#fff"/>
      </svg>
      <span>NOVA</span>
      <svg width="22" height="16" viewBox="0 0 22 16" aria-hidden="true">
        <path d="M1 5.5a14 14 0 0 1 20 0M4.5 9a9 9 0 0 1 13 0M8 12.5a4 4 0 0 1 6 0" fill="none" stroke="#fff" stroke-width="2.2" stroke-linecap="round"/>
        <circle cx="11" cy="14.5" r="1.5" fill="#fff"/>
      </svg>
    </div>
    <span class="status-time">4:21 PM</span>
    <div class="status-right">
      <svg width="12" height="20" viewBox="0 0 12 20" aria-hidden="true">
        <path d="M1 5l10 9-5 5V1l5 5-10 9" fill="none" stroke="#8fa3c4" stroke-width="1.5"/>
      </svg>
      <span>22%</span>
      <svg width="44" height="20" viewBox="0 0 44 20" aria-hidden="true">
        <rect x="1" y="1" width="38" height="18" rx="3" fill="none" stroke="#fff" stroke-width="1.5"/>
        <rect x="3.5" y="3.5" width="8" height="13" rx="1" fill="#fff"/>
        <rect x="40.5" y="7" width="2.5" height="6" rx="1" fill="#fff"/>
      </svg>
    </div>
  </header>

  <div class="brand-badge">
    <span class="brand-name">TAPLINE</span>
  </div>

  <form class="login-form">
    <div class="field">
      <svg width="26" height="26" viewBox="0 0 26 26" aria-hidden="true">
        <circle cx="13" cy="8" r="6" fill="none" stroke="#fff" stroke-width="1.6"/>
        <path d="M2 25v-2a8 8 0 0 1 8-8h6a8 8 0 0 1 8 8v2z" fill="none" stroke="#fff" stroke-width="1.6"/>
      </svg>
      <span>Username</span>
    </div>
    <div class="field">
      <svg width="26" height="30" viewBox="0 0 26 30" aria-hidden="true">
        <path d="M7 13V8a6 6 0 0 1 12 0v5" fill="none" stroke="#fff" stroke-width="1.6"/>
        <rect x="3" y="13" width="20" height="15" rx="1.5" fill="none" stroke="#fff" stroke-width="1.6"/>
        <circle cx="13" cy="19" r="2" fill="none" stroke="#fff" stroke-width="1.4"/>
        <path d="M13 21v3" stroke="#fff" stroke-width="1.4"/>
      </svg>
      <span>Password</span>
    </div>
    <div class="login-button">LOG IN</div>
    <p class="register-line">Don’t You Have An Account? <strong>Register Here</strong></p>
  </form>
</body>
</html>
```